West Halvern Commuter Coordination Association Needs an Ad Showcasing 2012's Accomplishments

The West Halvern Commuter Coordination Association is a nonprofit organization with the mission to foster transportation behaviors that benefit the community through advocacy, programs, education, and services. We have had a great year in 2012 and would like to show the community what we have accomplished.

We would like a FULL PAGE ad that will be used in a color print magazine and a black and white print publication.

The Pebble Tram - Over 75,000 trips taken by shuttle riders, a 120% increase in trips over 2011.

Stride Along Program - During the 2011-2012 school year an average of 897 students walked to school weekly on walk to school days.

Pedal Through Spring - 41,950 miles were ridden by students and teachers in May 2012 in 9 participating schools.

Wheel Fixer - over 600 bikes have been serviced in 2012.

Requirements
Must have
• Contact info:
West Halvern CCA
4127 Corliss Rd
Calverton, CA 95712
916-302-7718
WHCCA.org

Murmur @West HalvernCCA
Gatherly.com/WestHalvernCCA

LOGO

```html
<!DOCTYPE html>
<html lang="en">
<head>
<meta charset="utf-8">
<title>West Halvern CCA – Pointing You in a New Direction</title>
<link rel="stylesheet" href="https://fonts.googleapis.com/css2?family=Poiret+One&family=Open+Sans:wght@400;600;700&display=swap">
<style>
  :root {
    --frame: #cfcfcf;
    --sky: #1d71b8;
    --road: #5a51a2;
    --verge: #9cbf3b;
    --stripe: #f26b22;
    --footer: #a6b83b;
    --tangerine: #f47b2a;
    --amber: #f7931e;
    --marigold: #f9aa1c;
    --sun: #fcd116;
    --ink: #16437e;
    --white: #ffffff;
    --cream: #fdf6e3;
  }
  * { box-sizing: border-box; margin: 0; padding: 0; }
  html, body { width: 927px; height: 1200px; overflow: hidden; }
  body {
    background: var(--frame);
    font-family: "Open Sans", Arial, sans-serif;
    position: relative;
  }
  .ad { position: absolute; left: 14px; top: 14px; width: 899px; height: 1152px; }
  .sky { position: absolute; inset: 0 0 154px 0; background: var(--sky); }
  .footer {
    position: absolute; left: 0; right: 0; bottom: 0; height: 154px;
    background: var(--footer);
  }
  .road { position: absolute; left: -14px; top: -14px; width: 927px; height: 1200px; }

  .brand {
    position: absolute; left: 50px; top: 22px; width: 143px; height: 132px;
    background: var(--white);
    display: flex; flex-direction: column; align-items: center; justify-content: center;
    gap: 10px; text-align: center;
  }
  .brand-dot { width: 34px; height: 34px; border-radius: 50%; background: var(--ink); }
  .brand-name { font-weight: 700; font-size: 17px; line-height: 1.15; color: var(--ink); }

  .headline {
    position: absolute; left: 268px; top: 66px;
    font-family: "Poiret One", "Josefin Sans", sans-serif;
    color: var(--white); font-size: 62px; line-height: 66px;
    letter-spacing: 0; text-transform: uppercase; font-weight: 400;
    white-space: nowrap;
  }

  .stat {
    position: absolute; color: var(--white);
    border: 3px solid var(--white);
    font-size: 20px; line-height: 27px;
  }
  .stat h2 { font-size: 25px; line-height: 30px; font-weight: 700; }
  .stat--tram {
    left: 330px; top: 418px; width: 540px; height: 122px;
    background: var(--tangerine); text-align: right; padding: 16px 18px 0 20px;
    border-radius: 26px 10px 30px 14px / 12px 30px 16px 34px;
  }
  .stat--tram h2 { padding-right: 64px; }
  .stat--stride {
    left: 94px; top: 580px; width: 592px; height: 146px;
    background: var(--amber); padding: 14px 20px 0 12px;
    border-radius: 12px 34px 20px 30px / 28px 14px 36px 12px;
  }
  .stat--stride h2 { padding-left: 100px; }
  .stat--stride p:first-of-type { }
  .stat--stride .l1 { padding-left: 64px; display: block; }
  .stat--stride .l2 { padding-left: 30px; display: block; }
  .stat--pedal {
    left: 99px; top: 755px; width: 602px; height: 116px;
    background: var(--marigold); padding: 14px 20px 0 18px;
    border-radius: 30px 12px 24px 16px / 14px 32px 14px 30px;
  }
  .stat--fixer {
    left: 90px; top: 890px; width: 520px; height: 94px;
    background: var(--sun); padding: 10px 20px 0 18px;
    border-radius: 14px 28px 18px 26px / 26px 12px 30px 14px;
  }

  .social {
    position: absolute; left: 114px; top: 1060px;
    color: var(--cream); font-size: 21px; line-height: 31px;
  }
  .address {
    position: absolute; left: 539px; top: 1036px;
    color: var(--cream); font-size: 14px; line-height: 19px; font-style: normal;
  }
</style>
</head>
<body>
  <main class="ad">
    <div class="sky"></div>
    <div class="footer"></div>

    <svg class="road" viewBox="0 0 927 1200" role="img" aria-label="A curving road carrying pedestrians, cyclists, a car and a bus">
      <path fill="var(--verge)" d="M14,400 Q420,218 913,228 L913,250 Q420,244 14,434 Z"/>
      <path fill="var(--road)" d="M14,434 Q420,244 913,250 L913,366 Q440,356 14,648 Z"/>
      <path fill="var(--stripe)" d="M14,648 Q440,356 913,366 L913,382 Q440,378 14,672 Z"/>
    </svg>

    <div class="brand">
      <span class="brand-dot"></span>
      <span class="brand-name">West Halvern<br>CCA</span>
    </div>

    <h1 class="headline">Pointing You<br>In a New Direction</h1>

    <section class="stat stat--tram">
      <h2>The Pebble Tram -</h2>
      <p>Over 75,000 trips taken by shuttle riders<br>a 120% increase in trips over 2011.</p>
    </section>

    <section class="stat stat--stride">
      <h2>Stride Along Program -</h2>
      <p><span class="l1">During the 2011-2012 school year an average of</span><span class="l2">897 students walked to school weekly on walk to</span>school days.</p>
    </section>

    <section class="stat stat--pedal">
      <h2>Pedal Through Spring -</h2>
      <p>41,950 miles were ridden by students and teachers<br>in May 2012 in 9 participating schools</p>
    </section>

    <section class="stat stat--fixer">
      <h2>Wheel Fixer -</h2>
      <p>Over 600 bikes have been serviced in 2012.</p>
    </section>

    <div class="social">
      <p>Murmur @West HalvernCCA</p>
      <p>Gatherly.com/WestHalvernCCA</p>
    </div>

    <address class="address">
      West Halvern CCA 4127 Corliss Rd<br>
      Calverton, CA 95712<br>
      916-302-7718<br>
      WHCCA.org
    </address>
  </main>
</body>
</html>
```